Business Cards for Harborline Estates Partners, Inc.
Business Cards, Stationary, Etc.
Professional
Rocco Tamberlini
Broker
4710 SE Marigold Commons Lane
Suite 100
Coral Haven, Fl 33867
rocco@harborlinepfl.com
We prefer the use of icons, as opposed to wording for phone, fax, email.
I will need 2 options for each submission. The second option should allow for a picture to be inserted on the business card.
*Upon completion the winning designer will need to send a 2nd set of files, for another agent in the office. - Name, title, contact info to follow upon conclusion of Contest.

```html
<!DOCTYPE html>
<html lang="en">
<head>
<meta charset="utf-8">
<title>Harborline Estates Partners — Stationery</title>
<link href="https://fonts.googleapis.com/css2?family=Open+Sans:wght@400;700&display=swap" rel="stylesheet">
<style>
:root{
  --bg-dark:#2e2e2e;
  --bg-mid:#454545;
  --paper:#ffffff;
  --navy:#1f3a5a;
  --navy-deep:#142a44;
  --sky:#7fa6c9;
  --sage:#8b9a7f;
  --ink:#2b2b2b;
  --muted:#8a8f95;
  --caption:#9a9a9a;
  --watermark:#eef0f2;
  --fold:#dfe1e3;
  --photo:#9aa0a6;
}
*{margin:0;padding:0;box-sizing:border-box}
html,body{width:1200px;height:343px;overflow:hidden}
body{
  font-family:"Open Sans",Arial,sans-serif;
  background:radial-gradient(ellipse at 50% 40%,var(--bg-mid),var(--bg-dark));
  position:relative;color:var(--ink);
}
.piece{position:absolute;background:var(--paper);box-shadow:0 2px 5px rgba(0,0,0,.45);overflow:hidden}
.brand{display:flex;align-items:center;gap:4px;color:var(--navy);font-weight:700;line-height:1.05;text-transform:uppercase;white-space:nowrap}
.brand__mark{background:var(--navy);flex:none}
.band{position:absolute;left:0;bottom:0;width:100%}
.caption{position:absolute;font-size:5px;color:var(--caption);text-align:center}

/* master logo */
.master-brand{position:absolute;left:12px;top:68px}
.master-brand .brand{color:var(--paper);font-size:14px;gap:6px}
.master-brand .brand__mark{width:14px;height:14px;background:var(--paper)}
.master-brand small{font-size:8px}
.concept{position:absolute;left:12px;width:144px;top:110px;font-size:6px;color:var(--caption);text-align:center}

/* cards */
.card{width:144px;height:82px;left:12px}
.card--front{top:127px}
.card--back{top:232px}
.card .brand{position:absolute;left:8px;top:8px;font-size:7px}
.card .brand__mark{width:8px;height:8px}
.card__person{position:absolute;left:66px;top:26px;font-size:4.5px;line-height:1.4;white-space:nowrap}
.card__name{font-weight:700;color:var(--navy);font-size:5.5px}
.card__photo{position:absolute;left:8px;top:26px;width:28px;height:38px;background:linear-gradient(var(--photo),#6d7379)}
.card--back .card__person{left:44px}

/* letterheads */
.letterhead{top:19px;width:221px;height:312px}
.letterhead--one{left:163px}
.letterhead--two{left:403px}
.letterhead .brand{position:absolute;left:14px;top:16px;font-size:8px}
.letterhead .brand__mark{width:9px;height:9px}
.letterhead__contact{position:absolute;right:14px;top:15px;font-size:4px;line-height:1.5;color:var(--muted);white-space:nowrap}
.letterhead__watermark{position:absolute;left:0;width:100%;top:110px;text-align:center;font-weight:700;font-size:26px;line-height:1.1;color:var(--watermark);text-transform:uppercase}

/* envelopes */
.envelope{left:636px;width:192px;height:101px}
.envelope--one{top:67px}
.envelope--two{top:199px}
.envelope .brand{position:absolute;left:10px;top:10px;font-size:7px}
.envelope .brand__mark{width:8px;height:8px}
.envelope__addr{position:absolute;left:10px;top:28px;font-size:3.5px;color:var(--muted);line-height:1.5;white-space:nowrap}

/* envelope backs */
.env-back{left:897px;width:283px}
.env-back--sage{top:65px;height:62px}
.env-back--navy{top:132px;height:64px}
.env-back--white{top:201px;height:96px}
.env-back svg{position:absolute;inset:0;width:100%;height:100%}
.env-back .brand__mark{position:absolute;left:50%;margin-left:-4px;width:8px;height:8px}
</style>
</head>
<body>

<div class="master-brand">
  <div class="brand"><span class="brand__mark"></span><span>Harborline<br><small>Estates Partners</small></span></div>
</div>
<p class="concept">Stationery Concept</p>

<!-- business card front -->
<div class="piece card card--front">
  <div class="brand"><span class="brand__mark"></span><span>Harborline<br>Estates Partners</span></div>
  <div class="card__person">
    <p class="card__name">Rocco Tamberlini</p>
    <p>Broker</p>
    <p>4710 SE Marigold Commons Lane</p>
    <p>Suite 100, Coral Haven, Fl 33867</p>
    <p>&#9993; rocco@harborlinepfl.com</p>
  </div>
  <svg class="band" viewBox="0 0 144 14" height="14" preserveAspectRatio="none"><path d="M0 6 Q72 0 144 5 V14 H0Z" fill="var(--navy)"/><path d="M0 6 Q72 0 144 5" stroke="var(--sky)" stroke-width="1" fill="none"/></svg>
</div>
<p class="caption" style="left:12px;top:213px;width:144px">Business Card Front</p>

<!-- business card with photo -->
<div class="piece card card--back">
  <div class="brand"><span class="brand__mark"></span><span>Harborline<br>Estates Partners</span></div>
  <div class="card__photo" role="img" aria-label="Agent portrait photo area"></div>
  <div class="card__person">
    <p class="card__name">Rocco Tamberlini</p>
    <p>Broker</p>
    <p>4710 SE Marigold Commons Lane</p>
    <p>Suite 100, Coral Haven, Fl 33867</p>
    <p>&#9993; rocco@harborlinepfl.com</p>
  </div>
  <svg class="band" viewBox="0 0 144 12" height="12" preserveAspectRatio="none"><path d="M0 5 Q72 0 144 4 V12 H0Z" fill="var(--navy)"/></svg>
</div>
<p class="caption" style="left:12px;top:316px;width:144px">Business Card Back</p>

<!-- letterheads -->
<div class="piece letterhead letterhead--one">
  <div class="brand"><span class="brand__mark"></span><span>Harborline<br>Estates Partners</span></div>
  <div class="letterhead__contact"><p>4710 SE Marigold Commons Lane</p><p>Coral Haven, Fl 33867</p><p>&#9993; rocco@harborlinepfl.com</p></div>
  <p class="letterhead__watermark">Harborline<br>Estates</p>
  <svg class="band" viewBox="0 0 221 16" height="16" preserveAspectRatio="none"><path d="M0 7 Q110 0 221 6 V16 H0Z" fill="var(--navy)"/><path d="M0 7 Q110 0 221 6" stroke="var(--sky)" stroke-width="1" fill="none"/></svg>
</div>
<p class="caption" style="left:163px;top:333px;width:221px">Letterhead Page One</p>

<div class="piece letterhead letterhead--two">
  <div class="brand"><span class="brand__mark"></span><span>Harborline<br>Estates Partners</span></div>
  <p class="letterhead__watermark">Harborline<br>Estates</p>
  <svg class="band" viewBox="0 0 221 16" height="16" preserveAspectRatio="none"><path d="M0 7 Q110 0 221 6 V16 H0Z" fill="var(--navy)"/><path d="M0 7 Q110 0 221 6" stroke="var(--sky)" stroke-width="1" fill="none"/></svg>
</div>
<p class="caption" style="left:403px;top:333px;width:221px">Letterhead Page Two</p>

<!-- envelopes front -->
<div class="piece envelope envelope--one">
  <div class="brand"><span class="brand__mark"></span><span>Harborline<br>Estates Partners</span></div>
  <div class="envelope__addr"><p>4710 SE Marigold Commons Lane</p><p>Suite 100, Coral Haven, Fl 33867</p></div>
  <svg class="band" viewBox="0 0 192 12" height="12" preserveAspectRatio="none"><path d="M0 5 Q96 0 192 4 V12 H0Z" fill="var(--navy)"/><path d="M0 5 Q96 0 192 4" stroke="var(--sky)" stroke-width="1" fill="none"/></svg>
</div>
<p class="caption" style="left:636px;top:171px;width:192px">Envelope Front</p>

<div class="piece envelope envelope--two">
  <div class="brand"><span class="brand__mark"></span><span>Harborline<br>Estates Partners</span></div>
  <div class="envelope__addr"><p>4710 SE Marigold Commons Lane</p><p>Suite 100, Coral Haven, Fl 33867</p></div>
  <svg class="band" viewBox="0 0 192 12" height="12" preserveAspectRatio="none"><path d="M0 5 Q96 0 192 4 V12 H0Z" fill="var(--navy)"/></svg>
</div>
<p class="caption" style="left:636px;top:303px;width:192px">Envelope Front</p>

<!-- envelope backs -->
<div class="piece env-back env-back--sage">
  <svg viewBox="0 0 283 62" preserveAspectRatio="none"><path d="M0 62 L125 40 M283 62 L158 40" stroke="var(--fold)" stroke-width="1"/><path d="M0 0 H283 V6 L160 36 Q141.5 41 123 36 L0 6Z" fill="var(--sage)"/></svg>
  <span class="brand__mark" style="top:12px;background:var(--navy-deep)"></span>
</div>
<div class="piece env-back env-back--navy">
  <svg viewBox="0 0 283 64" preserveAspectRatio="none"><path d="M0 64 L125 42 M283 64 L158 42" stroke="var(--fold)" stroke-width="1"/><path d="M0 0 H283 V6 L160 37 Q141.5 42 123 37 L0 6Z" fill="var(--navy)"/></svg>
  <span class="brand__mark" style="top:12px;background:var(--paper)"></span>
</div>
<div class="piece env-back env-back--white">
  <svg viewBox="0 0 283 96" preserveAspectRatio="none"><path d="M0 6 L123 44 Q141.5 50 160 44 L283 6" stroke="#d6d8da" stroke-width="1" fill="none"/><path d="M0 96 L125 52 M283 96 L158 52" stroke="var(--fold)" stroke-width="1"/></svg>
  <span class="brand__mark" style="top:56px"></span>
</div>

</body>
</html>
```